Business Card Design for Real Estate Company

I am looking for a business card design that will catch my client's attention.

Industry/Entity Type

Business

Requirements
Must have
• Please have the following information in the business card design. You can substitute the "Office, Mobile, email, and web" with an icon or some other design you may think will go well with the business card.

Toma Verdi
482 W. Orchard Blvd., Suite 300
Pasadena, CA 91187
Office: 626.555.0147
Mobile: 626.555.0193
email: Toma@QuillStoneEstates.example
web: www.QuillStoneEstates.example

```html
<!DOCTYPE html>
<html lang="en">
<head>
<meta charset="utf-8">
<title>QuillStone Estates – Signs and Business Card</title>
<link href="https://fonts.googleapis.com/css2?family=Montserrat:wght@500;600;700&family=Source+Sans+3:wght@400;600&display=swap" rel="stylesheet">
<style>
  :root {
    --brand-red: #89201d;
    --card-red: #8a1d0c;
    --ink-red: #8a1f12;
    --ink-dark: #3a2a1c;
    --paper: #ffffff;
    --leaf-yellow: #e6d21a;
    --leaf-green: #a9b552;
    --leaf-orange: #ec8a2c;
    --leaf-blue: #4f8fc9;
    --shadow: rgba(0, 0, 0, 0.28);
  }
  * { box-sizing: border-box; margin: 0; padding: 0; }
  html, body { width: 1115px; height: 1200px; overflow: hidden; background: var(--paper); }
  .canvas { position: relative; width: 1115px; height: 1200px; }

  .sign {
    position: absolute; left: 66px; width: 686px; height: 173px;
    background: var(--brand-red);
    box-shadow: 1px 2px 3px var(--shadow);
    overflow: hidden;
  }
  .sign-text {
    position: absolute; top: 0; bottom: 0; left: 0; right: 140px;
    display: flex; align-items: center; justify-content: center;
    font-family: "Montserrat", sans-serif; font-weight: 600;
    color: var(--paper); white-space: nowrap; letter-spacing: -0.5px;
  }
  .sign--name { top: 69px; }
  .sign--name .sign-text { font-size: 82px; justify-content: flex-start; padding-left: 46px; }
  .sign--coming { top: 315px; }
  .sign--coming .sign-text { font-size: 63px; justify-content: flex-start; padding-left: 28px; }
  .sign--lease { top: 543px; }
  .sign--lease .sign-text { font-size: 82px; justify-content: flex-start; padding-left: 42px; }
  .sign--escrow { top: 770px; }
  .sign--escrow .sign-text { font-size: 78px; justify-content: flex-start; padding-left: 34px; word-spacing: 10px; }
  .sign--sold { top: 986px; }
  .sign--sold .sign-text { font-size: 112px; padding-left: 8px; }

  .leaf-art {
    position: absolute; right: 0; top: 14px; width: 124px; height: 159px;
    background:
      radial-gradient(circle at 40% 30%, var(--leaf-green) 0 13px, transparent 14px),
      radial-gradient(circle at 72% 26%, var(--leaf-yellow) 0 16px, transparent 17px),
      radial-gradient(circle at 52% 55%, var(--leaf-orange) 0 11px, transparent 12px),
      radial-gradient(circle at 22% 60%, var(--leaf-blue) 0 12px, transparent 13px),
      radial-gradient(circle at 32% 84%, var(--leaf-yellow) 0 12px, transparent 13px),
      radial-gradient(circle at 80% 8%, var(--leaf-blue) 0 10px, transparent 11px);
  }

  .card {
    position: absolute; left: 787px; width: 242px;
    box-shadow: 1px 2px 4px var(--shadow); overflow: hidden;
  }
  .card--front { top: 114px; height: 406px; background: var(--paper); text-align: center; }
  .card--back { top: 579px; height: 407px; background: var(--card-red); }

  .brand {
    font-family: "Montserrat", sans-serif; font-weight: 600;
    display: flex; align-items: center; justify-content: center; gap: 6px;
  }
  .brand-dot { width: 10px; height: 10px; border-radius: 50%; background: currentColor; }
  .card--front .brand { color: var(--ink-dark); font-size: 17px; margin-top: 58px; }
  .card--back .brand { color: var(--paper); font-size: 18px; position: absolute; top: 160px; left: 0; right: 0; }

  .agent-name {
    font-family: "Montserrat", sans-serif; font-weight: 600;
    color: var(--ink-red); font-size: 14px; margin-top: 42px;
  }
  .contact { font-family: "Source Sans 3", sans-serif; color: var(--ink-red); font-size: 11px; line-height: 16px; }
  .phones { margin-top: 6px; }
  .phone-line { display: flex; justify-content: center; align-items: center; gap: 5px; }
  .phone-line svg { width: 9px; height: 10px; fill: var(--ink-dark); }
  .address { color: var(--ink-dark); margin-top: 10px; line-height: 13px; }
  .web { margin-top: 9px; font-size: 9.5px; line-height: 15px; }

  .card--front .leaf-art { left: 0; right: auto; top: 272px; width: 140px; height: 106px; }
  .card--back .leaf-art { right: 0; top: 262px; width: 130px; height: 138px; }
  .card-band {
    position: absolute; left: 0; right: 0; bottom: 0; height: 28px;
    background: var(--card-red);
    font-family: "Source Sans 3", sans-serif; font-size: 10.5px; color: var(--paper);
    display: flex; align-items: center; justify-content: flex-end; padding-right: 24px;
  }
</style>
</head>
<body>
<main class="canvas">
  <section class="sign sign--name"><div class="sign-text">Toma Verdi</div><div class="leaf-art" role="img" aria-label="Colorful leaf branch illustration"></div></section>
  <section class="sign sign--coming"><div class="sign-text">COMING SOON</div><div class="leaf-art" role="img" aria-label="Colorful leaf branch illustration"></div></section>
  <section class="sign sign--lease"><div class="sign-text">FOR LEASE</div><div class="leaf-art" role="img" aria-label="Colorful leaf branch illustration"></div></section>
  <section class="sign sign--escrow"><div class="sign-text">IN ESCROW</div><div class="leaf-art" role="img" aria-label="Colorful leaf branch illustration"></div></section>
  <section class="sign sign--sold"><div class="sign-text">SOLD</div><div class="leaf-art" role="img" aria-label="Colorful leaf branch illustration"></div></section>

  <article class="card card--front">
    <div class="brand"><span class="brand-dot"></span>QuillStone Estates</div>
    <div class="agent-name">Toma Verdi</div>
    <div class="contact phones">
      <div class="phone-line"><svg viewBox="0 0 10 10" aria-hidden="true"><path d="M2 0.5 L3.6 2.6 L2.8 3.6 C3.4 5 4.8 6.5 6.3 7.2 L7.3 6.3 L9.5 7.9 L8.4 9.6 C4.5 9.4 0.6 5.5 0.4 1.6 Z"/></svg>626.555.0147</div>
      <div class="phone-line"><svg viewBox="0 0 10 10" aria-hidden="true"><path d="M2.5 0 H7.5 V10 H2.5 Z M3.4 1.2 V8 H6.6 V1.2 Z"/></svg>626.555.0193</div>
    </div>
    <div class="contact address">482 W. Orchard Blvd., Suite 300<br>Pasadena, CA 91187</div>
    <div class="contact web">Toma@QuillStoneEstates.example<br>www.QuillStoneEstates.example</div>
    <div class="leaf-art" role="img" aria-label="Colorful leaf branch illustration"></div>
    <div class="card-band">BRE Lic #01938245</div>
  </article>

  <article class="card card--back">
    <div class="brand"><span class="brand-dot"></span>QuillStone Estates</div>
    <div class="leaf-art" role="img" aria-label="Colorful leaf branch illustration"></div>
  </article>
</main>
</body>
</html>
```